Letterhead design of MERIDOR POWER KEEPER INC.

we are a energy saving company doing the solar screen, radian barrier, attic insulation, double panel windows. Basically i need the design of the letterhead including my company name, business address, phone numbers, fax number and email address. Main thing i need it look like a huge company and look like very high class. thanks !!

Reason: Please send me more new design about my company! Thanks so much!!

Industry/Entity Type

Business

```html
<!DOCTYPE html>
<html lang="en">
<head>
<meta charset="utf-8">
<title>Meridor Power Keeper Inc. — Letterhead</title>
<link rel="stylesheet" href="https://fonts.googleapis.com/css2?family=Libre+Baskerville&display=swap">
<style>
  :root {
    --page: #f6f6f6;
    --band: #e4e4e4;
    --band-light: #eeeeee;
    --footer: #dcdcdc;
    --ink: #6a6a6a;
    --ink-soft: #7a7a7a;
    --mark: #c9dbea;
    --glow-a: #e7eef5;
    --glow-b: #f3f3f3;
  }
  * { margin: 0; padding: 0; box-sizing: border-box; }
  html, body { width: 848px; height: 1200px; overflow: hidden; background: var(--page); }
  .letterhead {
    position: relative;
    width: 848px;
    height: 1200px;
    background: var(--page);
    font-family: "Libre Baskerville", "Baskerville", Georgia, serif;
    overflow: hidden;
  }
  .header-wave { position: absolute; top: 0; left: 0; width: 848px; height: 140px; }
  .brand {
    position: absolute;
    top: 26px;
    right: 14px;
    display: flex;
    align-items: center;
    gap: 12px;
  }
  .brand-dot {
    width: 34px;
    height: 34px;
    border-radius: 50%;
    background: var(--mark);
  }
  .brand-name {
    font-size: 22px;
    color: var(--ink);
    letter-spacing: 0.2px;
    white-space: nowrap;
  }
  .feature-art {
    position: absolute;
    left: 185px;
    top: 271px;
    width: 492px;
    height: 712px;
    border-radius: 40px;
    background: radial-gradient(ellipse at 45% 35%, var(--glow-a) 0%, var(--glow-b) 70%, var(--page) 100%);
  }
  .footer {
    position: absolute;
    left: 0;
    bottom: 0;
    width: 848px;
    height: 101px;
    background: var(--footer);
    display: flex;
    flex-direction: column;
    align-items: center;
    justify-content: center;
    gap: 9px;
    color: var(--ink-soft);
    font-size: 17px;
    line-height: 1.2;
    text-align: center;
  }
</style>
</head>
<body>
<div class="letterhead">
  <svg class="header-wave" viewBox="0 0 848 140" aria-hidden="true">
    <path d="M0 0 H848 V128 C720 132 610 118 500 98 C360 72 200 70 0 112 Z" fill="var(--band)"/>
    <path d="M0 112 C200 70 360 72 500 98 C380 84 220 88 0 126 Z" fill="var(--band-light)"/>
  </svg>

  <div class="brand">
    <span class="brand-dot"></span>
    <span class="brand-name">Meridor Power Keeper Inc.</span>
  </div>

  <div class="feature-art" role="img" aria-label="Large faint decorative brand motif in soft pale blue and grey"></div>

  <footer class="footer">
    <p class="footer-address">Address: 2280 Larkfield Ave Suite #310 Brenton, TEXAS 77590</p>
    <p class="footer-phone">Phone: # 555 214 0187;&nbsp; Fax: # 555 390 4261</p>
    <p class="footer-email">Email: meridorpowerkeeper@example.com</p>
  </footer>
</div>
</body>
</html>
```